Book Cover for Memoir: Sexual Assault and Traumatic Stress

I need a cover design for a memoir that is a victim's story of a sexual assault. I will need a print-on-demand cover, an eBook cover, and a 3D thumbnail image. The thumbnail and eBook cover will be used immediately, and the POD cover will be used in a few months with the full manuscript is ready. Therefore, I need an artist who is willing to make small adjustments if needed once the page count is set.

I have a image I have purchased that should give you an idea of the desired direction, but you can feel free to use your own images. I have attached some examples of book covers I like. I attached a color palette for fonts.

Overall Look: Fonts should be feminine and thin, but large to stand out. Look should be simple and elegant, and display and overall depressing feeling. There should be enough detail though to make it look professionally put together. Not TOO minimalistic.

I have also attached the Print Harbor templates if you choose to use those. If not, ensure there is an open place for the barcode on the bottom right.

Requirements
Must have
• Title: Beneath Quiet Rain
Subtitle: One Woman's Account of Fear, Guilt & Silence
Author: Dana Ruth Whitford
Audience: Mostly women 18-30
Quote (for the back): "I always thought I'd know how I'd react if I ever was raped. I was wrong. I've been wrong a lot lately."
Summary (back cover): When twenty-seven-year-old Dana Whitford wakes up with a gut-wrenching feeling, she has little memory of the horrifying events that occurred the night before. Days earlier, Dana was a spirited single mom who had abandoned her hometown to raise her daughter in the city and pursue her dreams. In the short months since Dana’s move to Seattle, she became the adored lover of a charismatic lawyer, started a new business, and finally felt life was going her way. So what happened to cause her to break?

In a gripping and heartbreaking narrative, Dana tells the true story of how her life unraveled from the traumatic events that took place that night and why what seems obvious to everyone else is impossible for Dana to believe. Beneath Quiet Rain is a chilling exploration of memory through trauma, trust in humanity, and a captivating story of strength and survival that appeals to the heart of fathers and mothers, sons and daughters, and men and women alike.
Nice to have
• BACK COVER: I'd like to have a photo on the back. This should depict the happy life of the main character before the sexual assault, and should be with her daughter. Or should be a nature scene that starts at the corner and blends into the rest of the cover. I have attached a possible image or you can use something you like.

```html
<!DOCTYPE html>
<html lang="en">
<head>
<meta charset="UTF-8">
<title>Beneath Quiet Rain — Cover Spread</title>
<link rel="stylesheet" href="https://fonts.googleapis.com/css2?family=Teko:wght@400&family=Oswald:wght@500&family=Open+Sans:wght@600&family=Nunito+Sans:wght@400&display=swap">
<style>
  :root {
    --backdrop: #ececec;
    --cover-black: #141414;
    --box-black: #0b0b0b;
    --title-grey: #bdbdbd;
    --title-white: #f4f4f4;
    --body-white: #e6e6e6;
    --label-grey: #cfcfcf;
    --wall-light: #ece6dc;
    --wall-warm: #d9cbb5;
    --sheet-white: #f7f7f5;
  }
  * { box-sizing: border-box; margin: 0; padding: 0; }
  html, body { width: 1200px; height: 800px; overflow: hidden; }
  body { background: var(--backdrop); }

  .canvas {
    position: relative; width: 1200px; height: 800px;
    display: flex; align-items: center; justify-content: center;
  }
  .cover-spread { display: flex; height: 540px; box-shadow: 0 10px 30px rgba(0,0,0,.18); }

  /* Back cover */
  .back-cover {
    width: 352px; height: 100%; background: var(--cover-black);
    padding: 18px 20px 22px; display: flex; flex-direction: column;
  }
  .back-author {
    align-self: flex-end; font-family: "Teko", sans-serif; font-size: 15px;
    letter-spacing: .5px; color: var(--title-grey); line-height: 1; text-transform: uppercase;
  }
  .back-title {
    font-family: "Teko", sans-serif; font-weight: 400; font-size: 46px; line-height: .9;
    color: var(--title-grey); text-transform: uppercase; text-align: center; margin-top: 4px;
    white-space: nowrap;
  }
  .back-subtitle {
    font-family: "Oswald", sans-serif; font-weight: 500; font-size: 11px; color: var(--title-white);
    text-transform: uppercase; text-align: center; margin-top: 6px; letter-spacing: .2px;
    white-space: nowrap;
  }
  .back-quote {
    font-family: "Nunito Sans", sans-serif; font-size: 10.6px; line-height: 1.42;
    color: var(--title-white); text-align: center; margin-top: 10px;
  }
  .back-blurb {
    font-family: "Nunito Sans", sans-serif; font-size: 10.6px; line-height: 1.42;
    color: var(--body-white); text-align: justify; margin-top: 8px;
  }
  .back-blurb p:last-child { text-align-last: center; }
  .back-footer { margin-top: auto; display: flex; justify-content: space-between; padding: 0 6px; }
  .placeholder-box {
    width: 118px; height: 54px; background: var(--box-black);
    display: flex; align-items: center; justify-content: center;
    font-family: "Nunito Sans", sans-serif; font-size: 11px; color: var(--label-grey); text-transform: uppercase;
  }

  /* Spine */
  .spine {
    width: 42px; height: 100%; background: var(--cover-black);
    display: flex; flex-direction: column; align-items: center; padding: 16px 0;
    border-left: 1px solid #222; border-right: 1px solid #222;
  }
  .spine-title, .spine-author { writing-mode: vertical-rl; text-transform: uppercase; }
  .spine-title { font-family: "Teko", sans-serif; font-size: 34px; line-height: 1; color: var(--title-grey); }
  .spine-author {
    margin-top: auto; font-family: "Open Sans", sans-serif; font-weight: 600;
    font-size: 10px; letter-spacing: 1px; color: var(--title-grey);
  }

  /* Front cover */
  .front-cover { width: 352px; height: 100%; background: var(--cover-black); display: flex; flex-direction: column; }
  .front-header { height: 136px; padding: 24px 14px 0; text-align: center; }
  .front-title {
    font-family: "Teko", sans-serif; font-weight: 400; font-size: 50px; line-height: .85;
    color: var(--title-white); text-transform: uppercase; white-space: nowrap;
  }
  .front-subtitle {
    font-family: "Oswald", sans-serif; font-weight: 500; font-size: 11.5px;
    color: var(--title-white); text-transform: uppercase; margin-top: 14px; white-space: nowrap;
  }
  .cover-photo {
    flex: 1;
    background: linear-gradient(180deg, var(--wall-light) 0%, var(--wall-warm) 55%, var(--sheet-white) 78%, #ffffff 100%);
  }
  .front-footer {
    height: 50px; display: flex; align-items: center; justify-content: center;
    font-family: "Open Sans", sans-serif; font-weight: 600; font-size: 13px;
    letter-spacing: .5px; color: var(--title-white); text-transform: uppercase;
  }
</style>
</head>
<body>
<main class="canvas">
  <section class="cover-spread">
    <article class="back-cover">
      <p class="back-author">Dana Ruth Whitford</p>
      <h2 class="back-title">Beneath Quiet Rain</h2>
      <p class="back-subtitle">One Woman's Account of Fear, Guilt &amp; Silence</p>
      <blockquote class="back-quote">"I always thought I'd know how I'd react if I ever was raped. I was wrong. I've been wrong a lot lately."</blockquote>
      <div class="back-blurb">
        <p>When twenty-seven-year-old Dana Whitford wakes up with a gut-wrenching feeling, she has little memory of the horrifying events that occurred the night before. Days earlier, Dana was a spirited single mom who had abandoned her hometown to raise her daughter in the city and pursue her dreams. In the short months since Dana's move to Seattle, she became the adored lover of a charismatic lawyer, started a new business, and finally felt life was going her way. So what happened to cause her to break?</p>
        <p>In a gripping and heartbreaking narrative, Dana tells the true story of how her life unraveled from the traumatic events that took place that night and why what seems obvious to everyone else is impossible for Dana to believe. Beneath Quiet Rain is a chilling exploration of memory through trauma, trust in humanity, and a captivating story of strength and survival that appeals to the heart of fathers and mothers, sons and daughters, and men and women alike.</p>
      </div>
      <div class="back-footer">
        <div class="placeholder-box">Logo</div>
        <div class="placeholder-box">ISBN</div>
      </div>
    </article>

    <div class="spine">
      <span class="spine-title">Beneath Quiet Rain</span>
      <span class="spine-author">Dana Ruth Whitford</span>
    </div>

    <article class="front-cover">
      <header class="front-header">
        <h1 class="front-title">Beneath Quiet Rain</h1>
        <p class="front-subtitle">One Woman's Account of Fear, Guilt &amp; Silence</p>
      </header>
      <div class="cover-photo" role="img" aria-label="Cover photograph: a woman sitting on white bed sheets with knees drawn up, against a warm pale wall"></div>
      <footer class="front-footer">Dana Ruth Whitford</footer>
    </article>
  </section>
</main>
</body>
</html>
```